Flyer-Design für Weihnachtsbäume als Dekoration
Zielgruppe
Wir bearbeiten Bleche nach Kundenvorgaben. Nebenbei stellen wir immer mal ein paar Dekoartikel
bzw. Sonderanfertigen her.
https://deinblechprofi.example/
http://www.kaltenwerk.example/
https://deinblechprofi.example/aktuelles/image-broschuere/
Mit diesem Flyer wollen wir für unsere Weihnachtsbäume werben. Die Preise sind Endpreis inkl. Mehrwertsteuer.
Aufgabenstellung
Ich hab noch mehr Bildmaterial zur Verfügung.

```html
<!DOCTYPE html>
<html lang="de">
<head>
<meta charset="utf-8">
<title>Flyer Deko-Weihnachtsbaum</title>
<link href="https://fonts.googleapis.com/css2?family=Oswald:wght@300;400&family=Open+Sans:wght@400;600&display=swap" rel="stylesheet">
<style>
  :root {
    --stage: #e6e6e6;
    --paper: #ffffff;
    --band: #8a8a8a;
    --band-wave: #9a9a9a;
    --text-light: #ffffff;
    --brand: #6d6d6d;
    --photo-a: #b9b6b1;
    --photo-b: #8f8c88;
    --inset-a: #8ea35c;
    --inset-b: #c7a14b;
  }
  * { margin: 0; padding: 0; box-sizing: border-box; }
  html, body { width: 1200px; height: 900px; overflow: hidden; background: var(--stage); }
  .canvas { position: relative; width: 1200px; height: 900px; }
  .flyer {
    position: absolute; left: 303px; top: 30px; width: 594px; height: 840px;
    background: var(--paper); overflow: hidden;
    box-shadow: 0 6px 24px rgba(0,0,0,.15);
  }
  .hero-photo {
    position: absolute; left: 0; top: 70px; width: 594px; height: 560px;
    background: linear-gradient(100deg, var(--photo-b) 0%, var(--photo-a) 30%, #dedbd6 60%, #f2f1ef 100%);
  }
  .inset-photo {
    position: absolute; left: 112px; top: 290px; width: 210px; height: 270px;
    border: 8px solid #fff;
    background: linear-gradient(160deg, var(--inset-a) 0%, var(--inset-b) 45%, #9aa08f 70%, #6f746c 100%);
    transform: rotate(-5deg);
    box-shadow: 0 3px 10px rgba(0,0,0,.25);
  }
  .title-band {
    position: absolute; left: 0; top: 70px; width: 500px; height: 150px;
    background: var(--band); display: flex; align-items: center; padding-left: 44px;
  }
  .title {
    font-family: "Oswald", sans-serif; font-weight: 300; color: var(--text-light);
    font-size: 52px; line-height: 1.02; letter-spacing: 0.5px;
  }
  .swoosh { position: absolute; left: 0; top: 540px; width: 594px; height: 300px; }
  .claim {
    position: absolute; left: 56px; top: 636px;
    font-family: "Oswald", sans-serif; font-weight: 300; color: var(--text-light);
    font-size: 30px; line-height: 1.25;
  }
  .brand {
    position: absolute; right: 40px; top: 712px; width: 210px; text-align: center;
    font-family: "Open Sans", sans-serif; color: var(--brand);
  }
  .brand-name { font-weight: 600; font-size: 26px; line-height: 1.1; }
  .brand-tag { font-size: 8px; letter-spacing: 1.5px; margin-top: 4px; }
  .partner { display: flex; align-items: center; justify-content: center; gap: 8px; margin-top: 16px; }
  .partner-mark { width: 20px; height: 20px; background: var(--brand); }
  .partner-name { font-weight: 600; font-size: 16px; }
</style>
</head>
<body>
<div class="canvas">
  <article class="flyer">
    <div class="hero-photo" role="img" aria-label="Foto: weißer Deko-Weihnachtsbaum aus Metall mit Kugeln vor einer grauen Wand"></div>
    <div class="inset-photo" role="img" aria-label="Foto: Metall-Weihnachtsbaum mit runden Aussparungen im Garten vor herbstlichen Bäumen"></div>
    <div class="title-band">
      <h1 class="title">DEKO-<br>WEIHNACHTSBAUM</h1>
    </div>
    <svg class="swoosh" viewBox="0 0 594 300" aria-hidden="true">
      <path d="M0 70 C160 60 420 40 594 0 L594 300 L0 300 Z" fill="var(--band-wave)"/>
      <path d="M0 300 L0 285 C200 260 340 120 594 80 L594 300 Z" fill="var(--paper)"/>
    </svg>
    <p class="claim">Innen &amp; Außen ...<br>ein Blickfang</p>
    <div class="brand">
      <div class="brand-name">Kaltenwerk</div>
      <div class="brand-tag">LASERSCHNEID &amp; ABKANTTECHNIK</div>
      <div class="partner">
        <span class="partner-mark"></span>
        <span class="partner-name">Vierlinden Metall</span>
      </div>
    </div>
  </article>
</div>
</body>
</html>
```